Classy Home Bar menu in word format

The name of the bar is Bar Penhallow
8x10 bar menu black/gold lettering
classy coloring/font. Cover page for who we are. Next 9 pages will be drinks
drinks need to have a spot for names - brief description and a box for a picture
Drink menu should have a speakeasy vibe and be at least 10 pages long with different layouts

Target Market(s)

Visitors to our home. Friends family and guests

Industry/Entity Type

Bar guests

Font styles to use
Script

Requirements
Must have
• Class, easily editable, spots for pictures

```html
<!DOCTYPE html>
<html lang="en">
<head>
<meta charset="utf-8">
<title>Bar Penhallow — Menu Pages</title>
<link rel="stylesheet" href="https://fonts.googleapis.com/css2?family=Alex+Brush&family=EB+Garamond:ital@1&family=Italianno&family=Sofia&display=swap">
<style>
  :root {
    --paper: #ffffff;
    --charcoal: #2f2d2c;
    --ink: #000000;
    --gold: #e6b06c;
    --gold-soft: rgba(230, 176, 108, 0.35);
    --lemon: #f1ec7c;
    --lemon-soft: rgba(241, 236, 124, 0.35);
  }
  html, body {
    margin: 0;
    padding: 0;
    overflow: hidden;
  }
  body {
    width: 748px;
    height: 1200px;
    background: var(--paper);
    position: relative;
  }
  .page {
    position: absolute;
  }
  .page--cover { left: 175px; top: 105px; width: 398px; height: 498px; background: var(--charcoal); }
  .page--martini { left: 41px; top: 672px; width: 321px; height: 401px; background: var(--charcoal); }
  .page--old-fashioned { left: 390px; top: 672px; width: 317px; height: 397px; background: var(--ink); }

  .linework {
    position: absolute;
    left: 0;
    top: 0;
    width: 748px;
    height: 1200px;
    pointer-events: none;
  }

  .text {
    position: absolute;
    margin: 0;
    text-align: center;
    white-space: nowrap;
    transform: translateX(-50%);
  }
  .cover-title {
    left: 374px; top: 266px;
    font-family: "Italianno", cursive;
    font-size: 44px; line-height: 1;
    color: var(--gold);
  }
  .cover-tagline {
    left: 374px; top: 313px;
    font-family: "EB Garamond", serif; font-style: italic;
    font-size: 13px; color: var(--gold);
  }
  .cover-intro {
    left: 374px; top: 493px;
    font-family: "EB Garamond", serif; font-style: italic;
    font-size: 9.5px; line-height: 16px; color: var(--gold);
  }
  .martini-brand {
    left: 202px; top: 713px;
    font-family: "Italianno", cursive;
    font-size: 21px; line-height: 1; color: var(--gold);
  }
  .martini-name {
    left: 202px; top: 757px;
    font-family: "Sofia", cursive;
    font-size: 28px; line-height: 35px; color: var(--gold);
  }
  .martini-desc {
    left: 202px; top: 862px;
    font-family: "EB Garamond", serif; font-style: italic;
    font-size: 8.5px; line-height: 13px; color: var(--gold);
  }
  .old-fashioned-name {
    left: 549px; top: 752px;
    font-family: "Alex Brush", cursive;
    font-size: 26px; line-height: 1; color: var(--lemon);
  }
  .old-fashioned-desc {
    left: 486px; top: 885px;
    font-family: "EB Garamond", serif; font-style: italic;
    font-size: 8.5px; line-height: 13px; color: var(--lemon);
  }

  .photo {
    position: absolute;
  }
  .photo--martini {
    left: 113px; top: 916px; width: 176px; height: 108px;
    background: radial-gradient(ellipse at 55% 55%, #c98a4a 0%, #6b5a52 22%, #1f3f7a 55%, #0b1430 100%);
  }
  .photo--old-fashioned {
    left: 562px; top: 828px; width: 98px; height: 155px;
    background: linear-gradient(170deg, #1c2330 0%, #3a2a1e 40%, #b06a24 68%, #d9a45a 100%);
  }
  .ornament {
    position: absolute;
    border-radius: 8px;
  }
  .ornament--cover { left: 338px; top: 380px; width: 72px; height: 17px; background: var(--gold-soft); }
  .ornament--martini { left: 182px; top: 838px; width: 40px; height: 12px; background: var(--gold-soft); }
  .ornament--old-fashioned { left: 530px; top: 785px; width: 38px; height: 10px; background: var(--lemon-soft); }
</style>
</head>
<body>
  <div class="page page--cover"></div>
  <div class="page page--martini"></div>
  <div class="page page--old-fashioned"></div>

  <svg class="linework" viewBox="0 0 748 1200" aria-hidden="true">
    <!-- Cover frames -->
    <path d="M222 130 H526 A19 19 0 0 0 545 149 V558 A19 19 0 0 0 526 577 H222 A19 19 0 0 0 203 558 V149 A19 19 0 0 0 222 130 Z" fill="none" stroke="var(--gold)" stroke-width="2.5"/>
    <rect x="223" y="155" width="298" height="400" fill="none" stroke="var(--gold)" stroke-width="0.6"/>
    <rect x="225.5" y="157.5" width="293" height="395" fill="none" stroke="var(--gold)" stroke-width="0.6"/>
    <line x1="286" y1="487" x2="461" y2="487" stroke="var(--gold)" stroke-width="0.7"/>
    <path d="M284 487 l2.5 -2.5 l2.5 2.5 l-2.5 2.5 Z M459 487 l2.5 -2.5 l2.5 2.5 l-2.5 2.5 Z" fill="var(--gold)"/>

    <!-- Martini page frames -->
    <path d="M78 692 H324 A15 15 0 0 0 339 707 V1037 A15 15 0 0 0 324 1052 H78 A15 15 0 0 0 63 1037 V707 A15 15 0 0 0 78 692 Z" fill="none" stroke="var(--gold)" stroke-width="2"/>
    <line x1="104" y1="843" x2="178" y2="843" stroke="var(--gold)" stroke-width="0.7"/>
    <line x1="224" y1="843" x2="298" y2="843" stroke="var(--gold)" stroke-width="0.7"/>
    <path d="M108 905 H294 A6 6 0 0 0 300 911 V1030 A6 6 0 0 0 294 1036 H108 A6 6 0 0 0 102 1030 V911 A6 6 0 0 0 108 905 Z" fill="none" stroke="var(--gold)" stroke-width="0.6"/>
    <path d="M109 908.5 H293 A4 4 0 0 0 296.5 912 V1029 A4 4 0 0 0 293 1032.5 H109 A4 4 0 0 0 105.5 1029 V912 A4 4 0 0 0 109 908.5 Z" fill="none" stroke="var(--gold)" stroke-width="0.6"/>

    <!-- Old Fashioned page frames -->
    <path d="M431 694 H665 A20 20 0 0 0 685 714 V1029 A20 20 0 0 0 665 1049 H431 A20 20 0 0 0 411 1029 V714 A20 20 0 0 0 431 694 Z" fill="none" stroke="var(--lemon)" stroke-width="1.2"/>
    <rect x="421" y="701" width="255" height="341" fill="none" stroke="var(--lemon)" stroke-width="0.6" stroke-dasharray="1.2 1.6"/>
    <line x1="444" y1="783" x2="653" y2="783" stroke="var(--lemon)" stroke-width="0.7"/>
    <line x1="549" y1="828" x2="549" y2="982" stroke="var(--lemon)" stroke-width="0.7"/>
    <path d="M522 1027.5 l2.5 2.5 l-2.5 2.5 l-2.5 -2.5 Z M573 1027.5 l2.5 2.5 l-2.5 2.5 l-2.5 -2.5 Z" fill="var(--lemon)"/>
    <path d="M534 1026 l4 4 l-4 4 l-4 -4 Z M561 1026 l4 4 l-4 4 l-4 -4 Z" fill="none" stroke="var(--lemon)" stroke-width="1.4"/>
  </svg>

  <!-- Cover -->
  <h1 class="text cover-title">Bar Penhallow</h1>
  <p class="text cover-tagline">A Speakeasy Experience</p>
  <div class="ornament ornament--cover" role="img" aria-label="Gold scrollwork flourish"></div>
  <p class="text cover-intro">Discover the allure of a bygone era at Bar<br>Penhallow, where exquisite concoctions and<br>timeless elegance converge.</p>

  <!-- Midnight Martini -->
  <p class="text martini-brand">Bar Penhallow</p>
  <h2 class="text martini-name">Midnight<br>Martini</h2>
  <div class="ornament ornament--martini" role="img" aria-label="Small gold scroll ornament"></div>
  <p class="text martini-desc">Smooth vodka or gin, shaken with vermouth and a twist<br>of lemon. Served in a chilled martini glass.</p>
  <div class="photo photo--martini" role="img" aria-label="Photo of a garnished cocktail glass against blue bokeh lights"></div>

  <!-- Old Fashioned -->
  <h2 class="text old-fashioned-name">The Classic Old Fashioned</h2>
  <div class="ornament ornament--old-fashioned" role="img" aria-label="Small scroll ornament"></div>
  <p class="text old-fashioned-desc">A blend of bourbon, bitters,<br>and a hint of orange essence,<br>stirred to perfection. Served<br>over a large ice cube.</p>
  <div class="photo photo--old-fashioned" role="img" aria-label="Photo of bourbon strained over a large ice cube with orange peel"></div>
</body>
</html>
```